資格は全部で2種類あります。
各々コースが2つに分かれており、それぞれ初級・中級・上級があります。
コース・級ごとに色合いを変えていただければと思っております。
※デザイン2種:各6色(2つのコース×3つの級)の色合い変更

今回はコンペ形式にて1種類のデザインを募集させていただきます。
採用させていただいた方には、2種類ともデザインしていただければと思っております。

また、認定証のデザインをもとにした、認定カードのデザインもお願いいたします。
※認定証同様、デザイン2種各6色の色合い変更

採用報酬は、認定証・認定カードのすべてのデザインを含めた金額になります。
今回のコンペでは、下記2点の認定証のデザインを募集させていただきます。
①「創造育成指導員」という資格の「発達障がい支援コース」の「初級」
②「デジタル匠指導員」という資格の「IT実践コース」の「初級」

記載いただきたい項目は下記の通りになります。

・初級
・認定証
・発達障がい支援アドバイザー
・●●殿
・●●年●月●日
・あなたは当カリキュラムを修了されましたので、『初級・発達障がい支援アドバイザー』として認定いたします。
・NPO法人青葉学習推進会

・初級
・認定証
・IT実践アシスタント
・●●殿
・●●年●月●日
・あなたは当カリキュラムを修了されましたので、『初級・IT実践アシスタント』として認定いたします。
・NPO法人青葉学習推進会
認定証はカミノハコにて発注予定となっているため、イラストレーターのデータにて納品いただきますようお願いいたします。
テンプレートにつきましては、下記ギガファイル便のデータをご確認ください。
https://files.examplestore-transfer.jp/1008-a71c2e9b40f35d8862e1c7a04b5f2913e

また、ロゴや認定証のサンプルを添付させていただきます。
イラストレーターのデータにつきましては下記ギガファイル便をご確認ください。
https://files.examplestore-transfer.jp/1005-3b8e0f41c92d7a65e0b1f4d82c6a07e15

ゴールドを差し色とした素敵なデザインであったので選ばせていただきました。
ありがとうございました。

この度は弊社のコンペにご参加いただきありがとうございました。
また機会がございましたら、よろしくお願いいたします。

```html
<!DOCTYPE html>
<html lang="ja">
<head>
<meta charset="UTF-8">
<title>認定証 初級 発達障がい支援アドバイザー</title>
<link rel="stylesheet" href="https://fonts.googleapis.com/css2?family=Shippori+Mincho:wght@500;700;800&display=swap">
<style>
  :root {
    --page: #ffffff;
    --gold-light: #f6e3a4;
    --gold: #d4a94a;
    --gold-deep: #a7772a;
    --brown: #8f4a1c;
    --brown-deep: #5e2c0d;
    --cream: #fffdf7;
    --ink: #3a2a1c;
    --muted: #6b5a4a;
    --title-red: #8a2a14;
    --crest-red: #c3271f;
    --crest-deep: #7e1410;
  }
  * { margin: 0; padding: 0; box-sizing: border-box; }
  html, body { width: 849px; height: 1200px; overflow: hidden; background: var(--page); }
  .certificate {
    position: relative;
    width: 849px;
    height: 1200px;
    font-family: "Shippori Mincho", serif;
    color: var(--ink);
  }
  .certificate__frame { position: absolute; inset: 0; }
  .issuer-mark {
    position: absolute;
    top: 168px; left: 0; right: 0;
    display: flex; justify-content: center; align-items: center; gap: 8px;
  }
  .issuer-mark__dot {
    width: 16px; height: 16px; border-radius: 50%;
    background: var(--crest-red);
  }
  .issuer-mark__name {
    font-weight: 700; font-size: 18px; color: var(--crest-deep); letter-spacing: 1px;
  }
  .cert-heading {
    position: absolute;
    top: 318px; left: 0; right: 0;
    text-align: center;
    font-weight: 700;
    font-size: 60px;
    line-height: 1.2;
    letter-spacing: 26px;
    padding-left: 26px;
    color: var(--ink);
  }
  .grade-crest {
    position: absolute;
    top: 412px; left: 349px;
    width: 150px; height: 138px;
    border-radius: 10px;
    background: radial-gradient(circle at 50% 42%, #d63a2c 0%, #a8241a 38%, #d4a94a 70%, #f3dc96 100%);
    display: flex; align-items: center; justify-content: center;
  }
  .grade-crest__label {
    font-weight: 700; font-size: 24px; color: #ffffff; letter-spacing: 1px;
    margin-top: -6px;
  }
  .qualification {
    position: absolute;
    top: 598px; left: 0; right: 0;
    text-align: center;
    font-weight: 700;
    font-size: 34px;
    line-height: 1.3;
    letter-spacing: 2px;
    color: var(--title-red);
  }
  .recipient {
    position: absolute;
    top: 688px; left: 232px; width: 385px;
    border-bottom: 1px solid var(--ink);
    height: 30px;
    text-align: right;
    font-size: 16px;
    padding-right: 6px;
  }
  .issue-date {
    position: absolute;
    top: 742px; left: 0; right: 0;
    text-align: center;
    font-size: 11px;
    letter-spacing: 22px;
    padding-left: 22px;
    color: var(--muted);
  }
  .statement {
    position: absolute;
    top: 810px; left: 0; right: 0;
    text-align: center;
    font-size: 15px;
    line-height: 1.85;
    font-weight: 500;
  }
  .issuer-ribbon { position: absolute; top: 905px; left: 288px; width: 274px; height: 56px; }
  .issuer-ribbon__label {
    position: absolute; inset: 0;
    display: flex; align-items: center; justify-content: center;
    font-weight: 700; font-size: 16px; letter-spacing: 1px; color: var(--brown-deep);
  }
</style>
</head>
<body>
<main class="certificate">
  <svg class="certificate__frame" width="849" height="1200" viewBox="0 0 849 1200">
    <defs>
      <linearGradient id="goldBorder" x1="0" y1="0" x2="1" y2="1">
        <stop offset="0" stop-color="#f8e7ac"/>
        <stop offset="0.35" stop-color="#c8973c"/>
        <stop offset="0.6" stop-color="#f3dc96"/>
        <stop offset="1" stop-color="#a7772a"/>
      </linearGradient>
      <radialGradient id="brownField" cx="0.5" cy="0.5" r="0.7">
        <stop offset="0" stop-color="#b0662a"/>
        <stop offset="0.7" stop-color="#8f4a1c"/>
        <stop offset="1" stop-color="#6a3210"/>
      </radialGradient>
    </defs>
    <rect x="55" y="58" width="740" height="1052" fill="url(#goldBorder)"/>
    <rect x="68" y="71" width="714" height="1026" fill="none" stroke="#fff3c8" stroke-width="1.5"/>
    <rect x="76" y="79" width="698" height="1010" fill="url(#brownField)" role="img" aria-label="茶色の地紋模様"/>
    <path d="M123 175 Q123 140 160 135 L330 135 Q380 112 425 98 Q470 112 520 135 L690 135 Q727 140 727 175
             L727 985 Q727 1015 690 1020 L520 1020 Q470 1040 425 1048 Q380 1040 330 1020 L160 1020 Q123 1015 123 985 Z"
          fill="url(#goldBorder)"/>
    <path d="M132 178 Q132 148 164 144 L333 144 Q382 122 425 108 Q468 122 517 144 L686 144 Q718 148 718 178
             L718 982 Q718 1008 686 1011 L517 1011 Q468 1030 425 1038 Q382 1030 333 1011 L164 1011 Q132 1008 132 982 Z"
          fill="#fffdf7"/>
    <path d="M144 184 Q144 158 170 155 L337 155 Q384 134 425 121 Q466 134 513 155 L680 155 Q706 158 706 184
             L706 978 Q706 998 680 1000 L513 1000 Q466 1018 425 1026 Q384 1018 337 1000 L170 1000 Q144 998 144 978 Z"
          fill="none" stroke="#d4a94a" stroke-width="1.5"/>
  </svg>

  <div class="issuer-mark">
    <span class="issuer-mark__dot"></span>
    <span class="issuer-mark__name">青葉学習推進会</span>
  </div>

  <h1 class="cert-heading">認定証</h1>

  <div class="grade-crest" role="img" aria-label="赤い盾と金色の月桂冠の級章">
    <span class="grade-crest__label">初級</span>
  </div>

  <h2 class="qualification">発達障がい支援アドバイザー</h2>

  <p class="recipient">殿</p>
  <p class="issue-date">年月日</p>

  <p class="statement">
    あなたは当カリキュラムを修了されましたので、<br>
    『初級・発達障がい支援アドバイザー』として認定いたします。
  </p>

  <div class="issuer-ribbon">
    <svg width="274" height="56" viewBox="0 0 274 56" aria-hidden="true">
      <defs>
        <linearGradient id="ribbonFill" x1="0" y1="0" x2="0" y2="1">
          <stop offset="0" stop-color="#f8e7ac"/>
          <stop offset="0.5" stop-color="#d4a94a"/>
          <stop offset="1" stop-color="#f3dc96"/>
        </linearGradient>
      </defs>
      <path d="M0 10 L24 10 L24 46 L0 46 L10 28 Z" fill="#b38232"/>
      <path d="M274 10 L250 10 L250 46 L274 46 L264 28 Z" fill="#b38232"/>
      <rect x="16" y="6" width="242" height="44" rx="4" fill="url(#ribbonFill)"/>
      <rect x="21" y="11" width="232" height="34" rx="3" fill="none" stroke="#fff3c8" stroke-width="1"/>
    </svg>
    <span class="issuer-ribbon__label">NPO法人青葉学習推進会</span>
  </div>
</main>
</body>
</html>
```